Velmora Builders LLC- Bus. Cards, Door Hangers, Invoice, Estimates, Postcards
I want a proffessional package that express who we are and what we do. www.velmora-builders.example
Velmora Builders LLC- Bus. Cards, Door Hangers, Invoice, Estimates, Postcards - Construction
Creative Brief
Professional
Calvin Tressel
Owner
4216 Pellham Ave. Denver, CO. 80417
calvin@velmora-builders.example
www.velmora-builders.example
Spray Foam Insulation Energy Auditing Weatherization Thermal Imaging

```html
<!DOCTYPE html>
<html lang="en">
<head>
<meta charset="utf-8">
<title>Velmora Builders – Business Card</title>
<link rel="stylesheet" href="https://fonts.googleapis.com/css2?family=Arimo:wght@400;700&display=swap">
<style>
  :root {
    --page-bg: #ffffff;
    --card-bg: #ffffff;
    --card-edge: #8a8a8a;
    --band-light: #8fcb3a;
    --band-mid: #4fa52c;
    --band-dark: #2c7d25;
    --band-shadow: #1d261c;
    --ink: #111111;
    --ink-soft: #3b3b3b;
    --brand-green: #4f9a2b;
  }
  * { margin: 0; padding: 0; box-sizing: border-box; }
  html, body {
    width: 1200px;
    height: 698px;
    overflow: hidden;
    background: var(--page-bg);
    font-family: "Arimo", Arial, sans-serif;
  }
  .business-card {
    position: relative;
    width: 1200px;
    height: 698px;
  }
  .card-shape {
    position: absolute;
    inset: 0;
  }
  .holder {
    position: absolute;
    top: 44px;
    right: 54px;
    text-align: right;
    color: var(--ink);
  }
  .holder-name {
    font-weight: 700;
    font-size: 29px;
    line-height: 36px;
  }
  .holder-title {
    font-size: 28px;
    line-height: 36px;
  }
  .brand {
    position: absolute;
    top: 328px;
    left: 0;
    width: 1200px;
    display: flex;
    flex-direction: column;
    align-items: center;
  }
  .brand-row {
    display: flex;
    align-items: center;
    gap: 18px;
  }
  .brand-mark {
    width: 58px;
    height: 58px;
    border-radius: 50%;
    background: var(--brand-green);
  }
  .brand-name {
    font-size: 64px;
    font-weight: 400;
    color: var(--ink-soft);
    letter-spacing: -1px;
    line-height: 72px;
  }
  .brand-tagline {
    margin-top: 6px;
    font-size: 13px;
    font-weight: 700;
    letter-spacing: 1.6px;
    color: var(--brand-green);
  }
  .contact {
    position: absolute;
    left: 72px;
    top: 498px;
    list-style: none;
    color: var(--ink);
    font-size: 27px;
    line-height: 34px;
  }
  .contact-label {
    display: inline-block;
    width: 40px;
  }
</style>
</head>
<body>
  <div class="business-card">
    <svg class="card-shape" width="1200" height="698" viewBox="0 0 1200 698" aria-hidden="true">
      <defs>
        <radialGradient id="bandGlow" cx="0.5" cy="0.05" r="0.6">
          <stop offset="0" stop-color="var(--band-light)"/>
          <stop offset="0.55" stop-color="var(--band-mid)"/>
          <stop offset="1" stop-color="var(--band-dark)"/>
        </radialGradient>
        <clipPath id="cardClip">
          <rect x="23" y="23" width="1154" height="652"/>
        </clipPath>
      </defs>
      <rect x="22.5" y="22.5" width="1155" height="653" fill="var(--card-bg)" stroke="var(--card-edge)" stroke-width="2"/>
      <g clip-path="url(#cardClip)">
        <path d="M28 92 Q28 200 132 200 H1068 Q1172 200 1172 92" fill="none" stroke="var(--band-shadow)" stroke-width="10"/>
        <path d="M23 23 H1177 V88 Q1177 190 1072 190 H128 Q23 190 23 88 Z" fill="url(#bandGlow)"/>
      </g>
    </svg>

    <div class="holder">
      <p class="holder-name">Calvin Tressel</p>
      <p class="holder-title">Owner</p>
    </div>

    <div class="brand">
      <div class="brand-row">
        <span class="brand-mark"></span>
        <span class="brand-name">Velmora Builders</span>
      </div>
      <p class="brand-tagline">Crafting Comfort And Lasting Value Room By Room</p>
    </div>

    <ul class="contact">
      <li>4216 Pellham Ave. Denver, CO. 80417</li>
      <li><span class="contact-label">P</span>:&nbsp; 720-555-0148</li>
      <li><span class="contact-label">E</span>:&nbsp; calvin@velmora-builders.example</li>
      <li><span class="contact-label">W</span>:&nbsp; www.velmora-builders.example</li>
    </ul>
  </div>
</body>
</html>
```